Fresh Tarrow Work Post - Business Card Required

Dear All,

I own Velmira Limited, which in turn owns the website:
www.harbinworkpost.example

I want all of you wonderful creative people to come up with a slick, and awesome business card design that incorporates the logo on the site, and some colouring and design elements from it.

You have free reign in how you go about doing this, I won't be giving my contact details on this platform, but the winner will be asked to redesign based on my contact details which I will supply at the end.

I need the design to be completed within 5 days. I need the final print copies of the business cards by the 25th November, so unfortunately it's a bit of a rush to get these designs ready.

Any questions, please ask.

Thank you
Updates

Thank you all for your hard work and exceptional designs provided. I do have to pick one, so I have a very clear idea of which one this is, however I will wait one further day until the competition closes to be fair to all those have submitted, or are in the process of submitting. I wish you all the best and thank you again for your dedication.

```html
<!DOCTYPE html>
<html lang="en">
<head>
<meta charset="utf-8">
<title>Harbin Work Post – Business Card</title>
<link href="https://fonts.googleapis.com/css2?family=Oswald:wght@400;600&display=swap" rel="stylesheet">
<style>
  :root {
    --backdrop: #d9d6d1;
    --card: #1c1c1c;
    --card-pattern-a: #151515;
    --card-pattern-b: #262626;
    --gold: #c9a03a;
    --gold-soft: #b48b2c;
  }
  * { margin: 0; padding: 0; box-sizing: border-box; }
  html, body {
    width: 1200px; height: 873px; overflow: hidden;
    background: var(--backdrop);
    font-family: "Oswald", "Arial Narrow", sans-serif;
  }
  .canvas { position: relative; width: 1200px; height: 873px; }

  .card {
    position: absolute;
    background: var(--card);
    box-shadow: 0 12px 30px rgba(0,0,0,.35);
    color: var(--gold);
  }

  /* Contact side (landscape) */
  .card--front { left: 70px; top: 290px; width: 540px; height: 310px; }
  .brand {
    display: flex; align-items: center; gap: 8px;
    font-weight: 600; text-transform: uppercase; letter-spacing: 2px;
    color: var(--gold);
  }
  .brand__dot { border-radius: 50%; background: var(--gold); flex: none; }
  .card--front .brand { position: absolute; right: 34px; top: 34px; font-size: 20px; }
  .card--front .brand__dot { width: 14px; height: 14px; }
  .brand-rule { position: absolute; right: 34px; top: 72px; width: 186px; height: 1px; background: var(--gold-soft); }

  .contact-list { position: absolute; left: 34px; top: 110px; list-style: none; font-size: 15px; line-height: 27px; }
  .contact-list li { display: flex; align-items: center; gap: 10px; }
  .contact-list svg { width: 13px; height: 13px; fill: var(--gold); flex: none; }

  .person { position: absolute; right: 34px; bottom: 34px; text-align: right; }
  .person__name { font-size: 26px; font-weight: 600; text-transform: uppercase; letter-spacing: 1px; line-height: 1.1; }
  .person__role { font-size: 14px; }

  /* Logo side (portrait) */
  .card--back { left: 700px; top: 165px; width: 380px; height: 540px; overflow: hidden; }
  .card__pattern {
    position: absolute; inset: 0;
    background: radial-gradient(circle at 50% 45%, var(--card-pattern-b), var(--card-pattern-a) 75%);
  }
  .card--back .brand-block {
    position: absolute; left: 0; right: 0; top: 50%; transform: translateY(-50%);
    display: flex; flex-direction: column; align-items: center; gap: 12px;
  }
  .card--back .brand { font-size: 30px; }
  .card--back .brand__dot { width: 20px; height: 20px; }
  .card--back .brand-rule-wide { width: 250px; height: 1px; background: var(--gold-soft); }
</style>
</head>
<body>
<main class="canvas">

  <section class="card card--front" aria-label="Business card, contact side">
    <div class="brand"><span class="brand__dot"></span>Harbin Work Post</div>
    <div class="brand-rule"></div>

    <ul class="contact-list">
      <li>
        <svg viewBox="0 0 24 24" aria-hidden="true"><path d="M6.6 10.8a15 15 0 0 0 6.6 6.6l2.2-2.2c.3-.3.7-.4 1-.2 1.1.4 2.3.6 3.6.6.6 0 1 .4 1 1V20c0 .6-.4 1-1 1A17 17 0 0 1 3 4c0-.6.4-1 1-1h3.5c.6 0 1 .4 1 1 0 1.3.2 2.5.6 3.6.1.3 0 .7-.2 1z"/></svg>
        0700 555 0142
      </li>
      <li>
        <svg viewBox="0 0 24 24" aria-hidden="true"><path d="M2 5h20v14H2zm2 2v.5l8 5 8-5V7z"/></svg>
        hello@harbinworkpost.example
      </li>
      <li>
        <svg viewBox="0 0 24 24" aria-hidden="true"><path d="M12 2a10 10 0 1 0 0 20 10 10 0 0 0 0-20zm0 2c1 1.3 1.8 3 2.1 5H9.9C10.2 7 11 5.3 12 4zM4.3 14a8 8 0 0 1 0-4h3.5a15 15 0 0 0 0 4zm5.6 0a13 13 0 0 1 0-4h4.2a13 13 0 0 1 0 4zm6.3 0a15 15 0 0 0 0-4h3.5a8 8 0 0 1 0 4zM12 20c-1-1.3-1.8-3-2.1-4h4.2c-.3 1-1.1 2.7-2.1 4z"/></svg>
        www.harbinworkpost.example
      </li>
      <li>
        <svg viewBox="0 0 24 24" aria-hidden="true"><path d="M12 2a7 7 0 0 0-7 7c0 5 7 13 7 13s7-8 7-13a7 7 0 0 0-7-7zm0 9.5a2.5 2.5 0 1 1 0-5 2.5 2.5 0 0 1 0 5z"/></svg>
        12 Quill Lane, Tarrow, TR4 9QX
      </li>
    </ul>

    <div class="person">
      <p class="person__name">Orwen Dace</p>
      <p class="person__role">Managing Director</p>
    </div>
  </section>

  <section class="card card--back" aria-label="Business card, brand side">
    <div class="card__pattern" role="img" aria-label="Dark tone-on-tone floral damask pattern"></div>
    <div class="brand-block">
      <div class="brand"><span class="brand__dot"></span>Harbin Work Post</div>
      <div class="brand-rule-wide"></div>
    </div>
  </section>

</main>
</body>
</html>
```